Corporate Branded Documents - IT Provider - On-going work

Hi, I'm Tom a Director of Harbourline IT Care a UK Based IT & Telecoms support firm. We've been trading for 12 years now and feel its time for a lick of paint. We have a logo, website etc but would like someone to create some standard documents for us.

- A PDF Proposal Template - We currently don't send our customers proposals as we have nothing that looks good.
- A Quote Template PDF - Example Attached
- A Order Template PDF - Example Attached
- A Invoice Template PDF - Example Attached
- A Generic Document PDF - Something we can use for customer application forms, NDA Agreements, Terms & Conditions etc

Our website can be found at www.harbourlineitcare.co.uk - here you'll get a feel for our branding. I've also attached 2 example documents - as well as our currently used documents. Hopefully you guys can see why it needs improving.

We'd also like to work with someone long term, these documents are a start but we'd like to make sure all the work we do looks and feels as smart as possible, so there is plenty of additional work available.

None of these templates need to be Print ready, 99% of the time it will be viewed digitally, so high resolution designs are best

Thanks,

Tom

Target Market(s)

Corporate & Educational Customers

Industry/Entity Type

It Support

Font styles to use
Sans Serif

Colors
ec1f27
0692cd
ffffff

```html
<!DOCTYPE html>
<html lang="en">
<head>
<meta charset="utf-8">
<title>Harbourline IT Care – Document Templates</title>
<link rel="stylesheet" href="https://fonts.googleapis.com/css2?family=Roboto:wght@400;500;700&display=swap">
<style>
:root{
  --red:#e2202a;
  --teal:#1a88a3;
  --teal-dark:#16718a;
  --ink:#333;
  --muted:#666;
  --grey-bg:#8e9095;
  --paper:#fff;
  --photo-a:#3f8c98;
  --photo-b:#cfe4e6;
}
*{box-sizing:border-box;margin:0;padding:0}
html,body{width:1200px;height:809px;overflow:hidden;background:var(--grey-bg);font-family:"Roboto",Arial,sans-serif;color:var(--ink)}
.canvas{position:relative;width:1200px;height:809px}
.page{position:absolute;width:265px;height:344px;background:var(--paper);box-shadow:2px 3px 5px rgba(0,0,0,.35);overflow:hidden}
.page::before{content:"";position:absolute;left:0;top:2px;width:226px;height:3px;background:var(--red)}
.page::after{content:"";position:absolute;left:228px;top:2px;width:37px;height:3px;background:var(--teal)}
.p1{left:51px;top:52px}.p2{left:329px;top:52px}.p3{left:610px;top:52px}.p4{left:890px;top:52px}
.p5{left:51px;top:410px}.p6{left:329px;top:410px}.p7{left:610px;top:410px}.p8{left:890px;top:410px}
.abs{position:absolute}
.footer{position:absolute;left:0;bottom:0;width:100%;height:19px;background:var(--teal);display:flex;align-items:center;padding:0 26px 0 30px;justify-content:space-between;color:#fff;font-size:3.4px;font-weight:700}
.footer .mark{position:absolute;right:0;top:0;width:19px;height:19px;background:var(--red)}
.photo{position:absolute;background:linear-gradient(160deg,var(--photo-a),#2d6f7a 45%,var(--photo-b))}
.photo.city{background:linear-gradient(120deg,#6b4a3a,#b49a86 45%,#dfe9ef)}
.photo.laptop{background:linear-gradient(120deg,#5f6670,#c9ccd0 60%,#eef0f2)}
.photo.net{background:linear-gradient(135deg,#0b1a4a,#1e5aa8 50%,#0d1d3d)}
.brand{font-weight:500;color:var(--teal);display:flex;align-items:center;gap:6px}
.brand .sq{background:var(--red);display:block}
h2.title{position:absolute;font-size:10.5px;font-weight:500;color:var(--teal)}
.sub{position:absolute;font-size:6px;color:var(--red)}
.sub.dark{color:#222}
.body{position:absolute;font-size:3.6px;line-height:1.45;color:#444}
.body p{margin-bottom:3px}
.body.lg{font-size:5.1px;line-height:1.65}
.red{color:var(--red)}
.blue{color:var(--teal)}
.hd{font-size:4px;color:var(--red);font-weight:500;text-transform:uppercase;margin-bottom:2px}
.list{position:absolute;list-style:none;font-size:5.2px;color:#555}
.list li{display:flex;align-items:center;gap:6px;height:10.4px}
.list li::before{content:"";width:6px;height:6px;background:var(--red);clip-path:polygon(0 0,100% 0,100% 100%,0 100%,0 0,25% 25%,25% 75%,75% 75%,75% 25%,25% 25%)}
.svc{position:absolute;left:164px;width:96px}
.svc .item{display:flex;gap:5px;margin-bottom:6px}
.svc .ic{width:8px;height:8px;border-radius:50%;background:var(--red);flex:none;margin-top:1px}
.svc b{display:block;font-size:6.4px;font-weight:400;color:var(--red);line-height:1.05}
.svc span{font-size:3.4px;color:#555;line-height:1.3;display:block}
.redbox{position:absolute;background:var(--red);color:#fff}
.circle{position:absolute;border-radius:50%;background:#c8c9cb}
.pct{font-size:9px;margin-top:6px}
.cap{position:absolute;text-align:center;font-size:3.2px;color:#555;width:42px}
.cap b{display:block;color:var(--red);font-weight:500;font-size:3.4px;margin-bottom:1px}
table.grid{position:absolute;left:16px;top:198px;width:232px;border-collapse:collapse;font-size:3.4px}
.grid th{background:var(--teal);color:#fff;font-weight:700;height:7px;font-size:3px}
.grid th.hot{background:var(--red)}
.grid th:first-child{background:none}
.grid td{height:13px;border-bottom:.5px solid #ccc;text-align:center}
.grid td:first-child{text-align:left;padding-left:8px;width:104px;color:#333;font-weight:500}
.grid svg{width:6px;height:6px;vertical-align:middle}
.band{position:absolute;left:0;top:58px;width:100%;height:66px;background:var(--red);color:#fff;font-size:5.6px;line-height:1.35;text-align:center;padding:11px 22px}
.member{position:absolute;width:70px;text-align:center}
.member .face{width:40px;height:40px;border-radius:50%;margin:0 auto 6px;background:linear-gradient(#dfe3e8,#6d7784);border:2px solid #fff;box-shadow:0 0 0 .5px #ccc}
.member b{display:block;font-size:5.6px;color:var(--red);font-weight:500}
.member span{font-size:4.8px;color:#444}
</style>
</head>
<body>
<svg width="0" height="0" style="position:absolute">
  <symbol id="tick" viewBox="0 0 10 10"><circle cx="5" cy="5" r="5" fill="#1a88a3"/><path d="M2.6 5.2l1.6 1.6 3.2-3.4" stroke="#fff" stroke-width="1.3" fill="none"/></symbol>
  <symbol id="cross" viewBox="0 0 10 10"><circle cx="5" cy="5" r="5" fill="#e2202a"/><path d="M3.2 3.2l3.6 3.6M6.8 3.2l-3.6 3.6" stroke="#fff" stroke-width="1.3"/></symbol>
</svg>

<main class="canvas">

  <!-- Cover -->
  <section class="page p1">
    <div class="brand abs" style="left:52px;top:36px;font-size:15px"><i class="sq" style="width:24px;height:24px"></i>Harbourline IT Care</div>
    <div class="photo" role="img" aria-label="Teal-toned photo of a lattice glass roof" style="left:0;top:94px;width:265px;height:231px"></div>
    <p class="abs" style="left:0;top:228px;width:100%;text-align:center;color:#fff;font-size:8.5px;line-height:1.4;font-weight:500">The 1st choice for IT<br>Managed Services</p>
    <footer class="footer"><span>Call Now: 0161 555 0192</span><span>hello@harbourlineitcare.co.uk</span><span>www.harbourlineitcare.co.uk</span><i class="mark"></i></footer>
  </section>

  <!-- Message from the Manager -->
  <section class="page p2">
    <h2 class="title" style="left:32px;top:37px">Message from the Manager</h2>
    <p class="sub dark" style="left:32px;top:51px">Sub heading or the key point or tagline.</p>
    <div class="abs" role="img" aria-label="Portrait photo placeholder of the manager" style="left:32px;top:72px;width:47px;height:50px;background:#dcdcdc"></div>
    <div class="body lg" style="left:88px;top:68px;width:140px">
      <p>Lorem ipsum is simply dummy text of the printing and typesetting industry. Lorem Ipsum has been the industry's standard dummy text ever since the 1500s, when an unknown printer took a galley of type and scrambled it to make a type spec book.</p>
      <p>It has survived not only five centuries, but also the leap into electronic typesetting, remaining essentially unchanged. It was popularised in the 1960s with the release of Letraset sheets containing Lorem Ipsum passages, and more recently with desktop publishing software like Aldus PageMaker include versions of Lorem Ipsum. Lorem Ipsum is simply dummy text of the printing and typesetting industry. Lorem Ipsum has been the industry's standard dummy text ever since the 1500s, when an unknown printer took a galley of type and scrambled it to make a type spec book.</p>
      <p>Regards,</p>
      <p class="red" style="margin-top:6px;font-size:6px">Manager Name</p>
    </div>
    <div class="abs" role="img" aria-label="Handwritten signature" style="left:88px;top:268px;width:110px;height:12px;border-bottom:.6px solid #999"></div>
    <footer class="footer"><span>Call Now: 0161 555 0192</span><span>hello@harbourlineitcare.co.uk</span><span>www.harbourlineitcare.co.uk</span><i class="mark"></i></footer>
  </section>

  <!-- How To Get Commitment -->
  <section class="page p3">
    <h2 class="title" style="left:20px;top:20px;color:var(--red)">How To Get Commitment</h2>
    <p class="sub" style="left:20px;top:34px;width:230px;line-height:1.3">Lorem Ipsum is simply dummy text of the printing and typesetting industry. Lorem Ipsum has been the industry's standard dummy.</p>
    <div class="body" style="left:20px;top:60px;width:230px">
      <p>Lorem ipsum is simply dummy text of the printing and typesetting industry. Lorem Ipsum has been the industry's standard dummy text ever since the 1500s, when an unknown printer took a galley of type and scrambled it to make a type specimen book. It has survived not only five centuries, but also the leap into electronic typesetting.</p>
      <p>Remaining essentially unchanged. It was popularised in the 1960s with the release of Letraset sheets containing Lorem Ipsum passages, and more recently with desktop publishing software like Aldus PageMaker including versions of Lorem Ipsum.</p>
      <p>Lorem ipsum is simply dummy text of the printing and typesetting industry. Lorem Ipsum has been the industry's standard dummy text ever since the 1500s.</p>
    </div>
    <div class="photo city" role="img" aria-label="Photo of a modern timber-clad building" style="left:21px;top:132px;width:129px;height:54px"></div>
    <p class="abs blue" style="left:21px;top:194px;width:135px;font-size:6px;line-height:1.35">Lorem ipsum Dolor has the expertise in the following key areas:</p>
    <ul class="list" style="left:21px;top:222px">
      <li>Design Build/Problem Solving</li><li>Storm and Process Water Systems</li><li>Heavy and Structural Concrete</li><li>Bridge Construction</li><li>Building Construction and Restoration</li><li>Hardscapes</li><li>All Civil Construction and Utility</li>
    </ul>
    <h3 class="abs blue" style="left:160px;top:144px;font-size:8.2px;font-weight:500">Services We Offer</h3>
    <div class="svc" style="top:164px">
      <div class="item"><i class="ic"></i><div><b>FINANCIAL</b><span>Lorem ipsum dolor sit amet, consectetur adipiscing elit incididunt.</span></div></div>
      <div class="item"><i class="ic"></i><div><b>WRITTEN<br>DOCUMENTS</b><span>Lorem ipsum dolor sit amet, consectetur adipiscing elit.</span></div></div>
      <div class="item"><i class="ic"></i><div><b>LOAN APPROVAL</b><span>Lorem ipsum dolor sit amet, consectetur adipiscing elit.</span></div></div>
      <div class="item"><i class="ic"></i><div><b>SCHEDULE<br>MANAGEMENT</b><span>Lorem ipsum dolor sit amet, consectetur adipiscing elit.</span></div></div>
      <div class="item"><i class="ic"></i><div><b>FUNDING</b><span>Lorem ipsum dolor sit amet, consectetur adipiscing elit.</span></div></div>
    </div>
    <footer class="footer"><span>Call Now: 0161 555 0192</span><span>hello@harbourlineitcare.co.uk</span><span>www.harbourlineitcare.co.uk</span><i class="mark"></i></footer>
  </section>

  <!-- Introduction -->
  <section class="page p4">
    <h2 class="title" style="left:19px;top:20px">Introduction</h2>
    <p class="sub" style="left:19px;top:34px">Subtitle following title</p>
    <div class="photo laptop" role="img" aria-label="Photo of hands working at a laptop" style="left:19px;top:52px;width:228px;height:52px"></div>
    <div class="redbox" style="left:19px;top:109px;width:68px;height:153px;padding:6px 7px;font-size:4.4px;line-height:1.3">
      <p>Lorem Ipsum is simply dummy text of the printing and typesetting industry. Lorem Ipsum has been the industry's standard dummy text ever since the 1500s, when an unknown</p>
      <p class="pct">50%</p><p style="font-size:3px">Lorem Ipsum is simply dummy text of the printing and typesetting industry.</p>
      <p class="pct">60%</p><p style="font-size:3px">Lorem Ipsum is simply dummy text of the printing and typesetting industry.</p>
    </div>
    <div class="body" style="left:101px;top:116px;width:146px">
      <p>Lorem ipsum is simply dummy text of the printing and typesetting industry. Lorem Ipsum has been the industry's standard dummy text ever since the 1500s, when an unknown printer took a galley of type and scrambled it to make a type specimen book. It has survived not only five centuries, but also the leap into electronic typesetting.</p>
      <p>Remaining essentially unchanged. It was popularised in the 1960s with the release of Letraset sheets containing Lorem Ipsum passages, and more recently with desktop publishing software like Aldus PageMaker including versions of Lorem Ipsum.</p>
      <p>Lorem ipsum is simply dummy text of the printing and typesetting industry. Lorem Ipsum has been the industry's standard dummy text ever since the 1500s.</p>
    </div>
    <i class="circle" style="left:111px;top:221px;width:28px;height:28px"></i>
    <i class="circle" style="left:159px;top:221px;width:28px;height:28px"></i>
    <i class="circle" style="left:207px;top:221px;width:28px;height:28px"></i>
    <p class="cap" style="left:104px;top:254px"><b>LOREM IPSUM</b>Lorem ipsum is simply dummy text of the printing.</p>
    <p class="cap" style="left:152px;top:254px"><b>LOREM IPSUM</b>Lorem ipsum is simply dummy text of the printing.</p>
    <p class="cap" style="left:200px;top:254px"><b>LOREM IPSUM</b>Lorem ipsum is simply dummy text of the printing.</p>
    <div class="circle" role="img" aria-label="Portrait of a team member" style="left:28px;top:278px;width:30px;height:30px;background:linear-gradient(#e6e8eb,#5e6874)"></div>
    <p class="abs" style="left:68px;top:278px;font-size:8px;color:#333">&ldquo;</p>
    <div class="body" style="left:78px;top:280px;width:168px;font-size:3.3px">Lorem ipsum is simply dummy text of the printing and typesetting industry. Lorem Ipsum has been the industry's standard dummy text ever since the 1500s, when an unknown printer took a galley of type and scrambled it to make a type specimen book. It has survived not only five centuries, but also the leap into electronic typesetting.</div>
    <footer class="footer"><span>Call Now: 0161 555 0192</span><span>hello@harbourlineitcare.co.uk</span><span>www.harbourlineitcare.co.uk</span><i class="mark"></i></footer>
  </section>

  <!-- Title page A -->
  <section class="page p5">
    <h2 class="title" style="left:16px;top:22px">Title for the Page</h2>
    <p class="sub" style="left:16px;top:36px">Subtitle following title</p>
    <div class="photo net" role="img" aria-label="Photo of glowing blue network lines" style="left:16px;top:67px;width:61px;height:58px"></div>
    <div class="body" style="left:86px;top:66px;width:160px">
      <p class="hd">Lorem ipsum dolor sit amet</p>
      <p>Lorem ipsum dolor sit amet, consectetur adipiscing elit, sed do eiusmod tempor incididunt ut labore et dolore magna aliqua. Ut enim ad minim veniam, quis nostrud exercitation ullamco laboris. Lorem ipsum dolor sit amet, consectetur adipiscing elit, sed do eiusmod tempor incididunt ut labore et dolore magna aliqua. Ut enim ad minim veniam, quis nostrud exercitation ullamco laboris.</p>
      <p>Lorem ipsum dolor sit amet, consectetur adipiscing elit, sed do eiusmod tempor incididunt ut labore et dolore magna aliqua. Ut enim ad minim veniam, quis nostrud exercitation ullamco laboris.</p>
    </div>
    <p class="abs blue" style="left:16px;top:135px;width:62px;font-size:4.3px;line-height:1.6">Lorem ipsum dolor sit amet, consectetur adipiscing elit, sed do eiusmod tempor incididunt ut labore et dolore magna aliqua. Ut enim ad minim</p>
    <p class="abs red" style="left:16px;top:225px;width:62px;font-size:4.3px;line-height:1.6">Lorem ipsum dolor sit amet, consectetur adipiscing elit, sed do eiusmod tempor incididunt ut labore et dolore magna aliqua. Ut enim ad minim</p>
    <div class="body" style="left:86px;top:154px;width:75px">
      <p class="hd">Smart, simple, effective</p>
      <p>Sed ut perspiciatis unde omnis iste natus error sit voluptatem accusantium doloremque laudantium, totam rem aperiam, eaque ipsa quae ab illo inventore veritatis et quasi architecto beatae vitae dicta sunt explicabo. Nemo enim ipsam voluptatem quia voluptas sit aspernatur aut odit aut fugit, sed quia consequuntur magni dolores eos qui ratione voluptatem.</p>
      <p class="hd" style="margin-top:5px">Flexible learning</p>
      <p>Sed ut perspiciatis unde omnis iste natus error sit voluptatem accusantium doloremque laudantium, totam rem aperiam, eaque ipsa quae ab illo inventore veritatis et quasi architecto beatae vitae dicta sunt explicabo. Nemo enim ipsam voluptatem quia voluptas sit aspernatur aut odit aut fugit, sed quia consequuntur magni dolores eos qui ratione voluptatem.</p>
    </div>
    <div class="photo" role="img" aria-label="Teal-toned photo of a lattice glass roof" style="left:167px;top:152px;width:75px;height:63px"></div>
    <div class="body" style="left:167px;top:223px;width:80px">
      <p class="hd">Personalized tutoring</p>
      <p>Sed ut perspiciatis unde omnis iste natus error sit voluptatem accusantium doloremque laudantium, totam rem aperiam, eaque ipsa quae ab illo inventore veritatis et quasi architecto beatae vitae dicta sunt explicabo. Nemo enim ipsam voluptatem quia voluptas sit aspernatur aut odit aut fugit, sed quia consequuntur magni dolores eos qui ratione voluptatem sequi nesciunt.</p>
    </div>
    <footer class="footer"><span>Call Now: 0161 555 0192</span><span>hello@harbourlineitcare.co.uk</span><span>www.harbourlineitcare.co.uk</span><i class="mark"></i></footer>
  </section>

  <!-- Title page B -->
  <section class="page p6">
    <h2 class="title" style="left:16px;top:22px">Title for the Page</h2>
    <p class="sub" style="left:16px;top:36px">Subtitle following title</p>
    <div class="photo net" role="img" aria-label="Photo of glowing network light trails" style="left:16px;top:53px;width:131px;height:66px"></div>
    <div class="photo" role="img" aria-label="Teal-toned photo of a lattice glass roof" style="left:155px;top:53px;width:131px;height:66px;width:130px"></div>
    <div class="body" style="left:16px;top:124px;width:112px">
      <p class="hd">Lorem ipsum dolor sit amet</p>
      <p>Lorem ipsum dolor sit amet, consectetur adipiscing elit, sed do eiusmod tempor incididunt ut labore et dolore magna aliqua. Ut enim ad minim veniam, quis nostrud exercitation ullamco laboris. Lorem ipsum dolor sit amet, consectetur adipiscing elit, sed do eiusmod tempor incididunt ut labore et dolore magna aliqua. Ut enim ad minim veniam, quis nostrud exercitation ullamco laboris.</p>
    </div>
    <div class="body" style="left:135px;top:130px;width:112px">
      <p>Lorem ipsum dolor sit amet, consectetur adipiscing elit, sed do eiusmod tempor incididunt ut labore et dolore magna aliqua. Ut enim ad minim veniam, quis nostrud exercitation ullamco laboris. Lorem ipsum dolor sit amet, consectetur adipiscing elit, sed do eiusmod tempor incididunt ut labore et dolore magna aliqua. Ut enim ad minim veniam, quis nostrud exercitation ullamco laboris.</p>
    </div>
    <table class="grid">
      <thead><tr><th></th><th>SERVICE</th><th>SERVICE</th><th>SERVICE</th><th class="hot">SERVICE</th></tr></thead>
      <tbody>
        <tr><td>Lorem ipsum is simply</td><td><svg><use href="#tick"/></svg></td><td><svg><use href="#tick"/></svg></td><td><svg><use href="#tick"/></svg></td><td><svg><use href="#tick"/></svg></td></tr>
        <tr><td>Lorem ipsum is simply</td><td><svg><use href="#cross"/></svg></td><td><svg><use href="#tick"/></svg></td><td><svg><use href="#tick"/></svg></td><td><svg><use href="#tick"/></svg></td></tr>
        <tr><td>Lorem ipsum is simply</td><td><svg><use href="#cross"/></svg></td><td><svg><use href="#tick"/></svg></td><td><svg><use href="#tick"/></svg></td><td><svg><use href="#tick"/></svg></td></tr>
        <tr><td>Lorem ipsum is simply</td><td><svg><use href="#cross"/></svg></td><td><svg><use href="#tick"/></svg></td><td><svg><use href="#tick"/></svg></td><td><svg><use href="#tick"/></svg></td></tr>
        <tr><td>Lorem ipsum is simply</td><td><svg><use href="#cross"/></svg></td><td><svg><use href="#cross"/></svg></td><td><svg><use href="#tick"/></svg></td><td><svg><use href="#tick"/></svg></td></tr>
        <tr><td>Lorem ipsum is simply</td><td><svg><use href="#cross"/></svg></td><td><svg><use href="#cross"/></svg></td><td><svg><use href="#cross"/></svg></td><td><svg><use href="#tick"/></svg></td></tr>
        <tr><td>Lorem ipsum is simply</td><td><svg><use href="#cross"/></svg></td><td><svg><use href="#cross"/></svg></td><td><svg><use href="#cross"/></svg></td><td><svg><use href="#tick"/></svg></td></tr>
      </tbody>
    </table>
    <footer class="footer"><span>Call Now: 0161 555 0192</span><span>hello@harbourlineitcare.co.uk</span><span>www.harbourlineitcare.co.uk</span><i class="mark"></i></footer>
  </section>

  <!-- Team -->
  <section class="page p7">
    <h2 class="title" style="left:0;top:28px;width:100%;text-align:center">Lorem Ipsum Dolor Sit Emet Is a Summy</h2>
    <div class="band">Lorem Ipsum is simply dummy text of the printing and typesetting industry. Lorem Ipsum has been the industry's standard dummy text ever since the 1500s. Ipsum.</div>
    <div class="member" style="left:13px;top:96px"><div class="face" role="img" aria-label="Team member portrait"></div><b>NAME HERE</b><span>Managing Partner</span></div>
    <div class="member" style="left:97px;top:96px"><div class="face" role="img" aria-label="Team member portrait"></div><b>NAME HERE</b><span>Managing Partner</span></div>
    <div class="member" style="left:180px;top:96px"><div class="face" role="img" aria-label="Team member portrait"></div><b>NAME HERE</b><span>Managing Partner</span></div>
    <div class="member" style="left:13px;top:180px"><div class="face" role="img" aria-label="Team member portrait"></div><b>NAME HERE</b><span>Managing Partner</span></div>
    <div class="member" style="left:97px;top:180px"><div class="face" role="img" aria-label="Team member portrait"></div><b>NAME HERE</b><span>Managing Partner</span></div>
    <div class="member" style="left:180px;top:180px"><div class="face" role="img" aria-label="Team member portrait"></div><b>NAME HERE</b><span>Managing Partner</span></div>
    <footer class="footer"><span>Call Now: 0161 555 0192</span><span>hello@harbourlineitcare.co.uk</span><span>www.harbourlineitcare.co.uk</span><i class="mark"></i></footer>
  </section>

  <!-- Back cover -->
  <section class="page p8">
    <div class="photo" role="img" aria-label="Teal-toned photo of a lattice glass roof" style="left:0;top:0;width:265px;height:235px"></div>
    <div class="brand abs" style="left:82px;top:265px;font-size:11px"><i class="sq" style="width:18px;height:18px"></i>Harbourline IT Care</div>
    <footer class="footer"><span>Call Now: 0161 555 0192</span><span>hello@harbourlineitcare.co.uk</span><span>www.harbourlineitcare.co.uk</span><i class="mark"></i></footer>
  </section>

</main>
</body>
</html>
```